Cannabis Company needs a packaging design for a 4x6 pouch

We need a design for a new cannabis company. Included is the logo in red. The logo color can change. Whatever color looks best with the design is what we'll use. The design can't include any cartoon characters or anything that may appeal to children. We have multiple products that are similar that will be using the same design. The pouch will contain 10 pyramid shaped gummies. The look we're going for is modern, simple, but eye catching. I included a handful of photos of packaging we like if that helps.

```html
<!DOCTYPE html>
<html lang="en">
<head>
<meta charset="utf-8">
<title>Gummies Pouch</title>
<link href="https://fonts.googleapis.com/css2?family=Alfa+Slab+One&family=Playball&family=Josefin+Sans:wght@600&display=swap" rel="stylesheet">
<style>
  :root {
    --leaf-dark: #1f3a14;
    --leaf-mid: #3f7a26;
    --leaf-light: #6aa83a;
    --cream-top: #f8e6b0;
    --tan-rim: #c8a55c;
    --label-cream: #fdf6dc;
    --badge-cream: #fbeec4;
    --ink-green: #3f4a2e;
    --dash: #9a9a8a;
    --white: #ffffff;
  }
  * { margin: 0; padding: 0; box-sizing: border-box; }
  html, body { width: 801px; height: 1200px; overflow: hidden; background: #fff; }
  .pouch { position: relative; width: 801px; height: 1200px; overflow: hidden; }
  .leaf-backdrop {
    position: absolute; inset: 0;
    background: radial-gradient(circle at 30% 60%, var(--leaf-light), var(--leaf-mid) 45%, var(--leaf-dark) 100%);
  }
  .top-band { position: absolute; left: 0; top: 0; width: 801px; height: 460px; }
  .brand-badge {
    position: absolute; left: 255px; top: 271px; width: 293px; height: 222px;
    background: var(--badge-cream); border: 3px solid var(--tan-rim); border-radius: 14px;
    display: flex; align-items: center; justify-content: center; gap: 14px;
  }
  .brand-dot { width: 26px; height: 26px; border-radius: 50%; background: var(--ink-green); }
  .brand-name {
    font-family: "Josefin Sans", sans-serif; font-weight: 600; font-size: 54px;
    color: var(--ink-green); letter-spacing: 1px;
  }
  .product-label {
    position: absolute; left: 166px; top: 554px; width: 468px; height: 540px;
    background: var(--label-cream); border-radius: 22px;
  }
  .product-label__frame {
    position: absolute; inset: 28px; border: 3px dashed var(--dash); border-radius: 10px;
  }
  .product-name {
    position: absolute; left: 0; right: 0; top: 104px; text-align: center;
    font-family: "Alfa Slab One", serif; font-size: 86px; line-height: 1;
    color: var(--ink-green); letter-spacing: 2px;
  }
  .product-type {
    position: absolute; left: 0; right: 0; top: 208px; text-align: center;
    font-family: "Playball", cursive; font-size: 76px; line-height: 1;
    color: var(--ink-green);
  }
  .product-count {
    position: absolute; left: 0; right: 0; top: 400px; text-align: center;
    font-family: "Playball", cursive; font-size: 34px; color: var(--ink-green);
  }
  .net-weight {
    position: absolute; left: 236px; top: 1128px;
    font-family: Arial, Helvetica, sans-serif; font-size: 27px; color: var(--white);
  }
</style>
</head>
<body>
<main class="pouch">
  <div class="leaf-backdrop" role="img" aria-label="Dense pattern of green cannabis leaves covering the pouch background"></div>

  <svg class="top-band" viewBox="0 0 801 460" aria-hidden="true">
    <path d="M0 0 H801 V390 Q400 445 0 390 Z" fill="var(--tan-rim)"/>
    <path d="M0 0 H801 V263 Q400 460 0 263 Z" fill="var(--cream-top)"/>
  </svg>

  <div class="brand-badge">
    <span class="brand-dot"></span>
    <span class="brand-name">leafora</span>
  </div>

  <section class="product-label">
    <div class="product-label__frame"></div>
    <h1 class="product-name">CDB</h1>
    <p class="product-type">Gummies</p>
    <p class="product-count">10 pcs</p>
  </section>

  <p class="net-weight">Net Weight:</p>
</main>
</body>
</html>
```